I need a flyer designed for a marine service company. Our company specializes in boat engine diagnostic/repair, engine service, electronic installation and repairs, bottom paint, detailing, winterization and shrink wrapping. We would like to see designs that incorporate our color scheme of deep blue, blueish gray and black (please see attached photo)

Target Market(s)

Boat owners

Industry/Entity Type

Marine

Logo Text

Kelpridge Harbor Services

Requirements
Must have
• Company logo
Nice to have
• List the services we provide.

```html
<!DOCTYPE html>
<html lang="en">
<head>
<meta charset="utf-8">
<title>Kelpridge Harbor Services – Flyer Designs</title>
<link rel="stylesheet" href="https://fonts.googleapis.com/css2?family=Cinzel:wght@400;600&family=Montserrat:ital,wght@0,400;0,600;0,700;1,500&display=swap">
<style>
  :root{
    --stage:#8a8c90;
    --navy:#1d2c57;
    --deep:#142047;
    --ink:#1f2d55;
    --sky:#7f9fd9;
    --sky-soft:#a9bfe8;
    --steel:#5c6f9b;
    --white:#ffffff;
    --call:#4f7fd1;
  }
  *{box-sizing:border-box;margin:0;padding:0}
  html,body{width:1200px;height:330px;overflow:hidden;background:var(--stage);font-family:"Montserrat",sans-serif}
  .board{position:relative;width:1200px;height:330px}
  .label{position:absolute;top:7px;width:216px;text-align:center;color:var(--white);font-weight:700;font-size:10px;letter-spacing:.3px}
  .sheet{position:absolute;top:25px;width:216px;height:280px;box-shadow:0 3px 6px rgba(0,0,0,.35);overflow:hidden}
  .flyer{position:absolute;left:0;top:0;width:463px;height:600px;transform:scale(.4665);transform-origin:0 0;background:var(--white);overflow:hidden;color:var(--white)}

  .photo{position:absolute;left:0;top:40px;width:463px;height:360px}
  .photo--speedboat{background:linear-gradient(160deg,#2c4778 0%,#3d5f96 40%,#1e3562 100%)}
  .photo--yacht{background:linear-gradient(180deg,#e8ecf1 0%,#c9d2dc 45%,#8b97a6 100%)}
  .photo--harbor{background:linear-gradient(180deg,#f2d27a 0%,#f4b95a 35%,#6d86a4 60%,#2f4668 100%)}
  .photo--sail{background:linear-gradient(180deg,#41536f 0%,#c79a5c 40%,#f0b860 52%,#4a5e7a 75%,#263a5e 100%)}
  .photo--engine{background:linear-gradient(160deg,#9aa3ad 0%,#6f7985 45%,#3e4754 100%);top:0;height:300px}

  .shapes{position:absolute;left:0;top:0;width:463px;height:600px}

  .logo{position:absolute;left:22px;top:12px;width:140px;text-align:center;color:var(--ink)}
  .logo__mark{display:block;width:34px;height:34px;margin:0 auto 6px;border:3px solid var(--ink);border-radius:50%}
  .logo__name{font-family:"Cinzel",serif;font-size:15px;font-weight:400;line-height:1.1}

  .contact-top{position:absolute;right:29px;top:18px;text-align:right}
  .contact-top__lead{color:var(--ink);font-size:12.5px;font-weight:600}
  .contact-top__call{color:var(--call);font-size:17.5px;font-weight:700;margin-top:2px}

  .headline{position:absolute;font-family:"Cinzel",serif;line-height:1;color:var(--ink)}
  .headline span{display:block}
  .headline--stacked{left:300px;top:152px;color:var(--white);text-align:center;font-size:28px}
  .headline--stacked .headline__small{font-size:17px;margin-bottom:4px}
  .headline--wide{left:205px;top:122px;font-size:23px}
  .headline--sail{left:228px;top:148px}
  .headline--engine{left:245px;top:34px;color:var(--white);text-align:center;font-size:27px;line-height:1.05}

  .circle{position:absolute;border-radius:50%;border:5px solid var(--white);box-shadow:0 2px 6px rgba(0,0,0,.35)}
  .circle--hull{left:188px;top:226px;width:144px;height:144px;background:linear-gradient(160deg,#a9c2de 0%,#e9eef4 50%,#3c5272 100%)}
  .circle--runabout{left:318px;top:240px;width:132px;height:132px;background:linear-gradient(180deg,#9fb7d1 0%,#dfe6ee 45%,#8c2f35 70%,#3e4e62 100%)}
  .circle--alternator{left:188px;top:122px;width:136px;height:136px;background:linear-gradient(150deg,#1f5c63 0%,#5f8a8c 50%,#22343b 100%)}
  .circle--polisher{left:316px;top:150px;width:120px;height:120px;background:linear-gradient(150deg,#f2f4f6 0%,#e8d04a 45%,#3fa2c4 80%)}

  .tab{position:absolute;height:24px;background:var(--sky);color:var(--white);font-size:15px;font-weight:500;line-height:24px;letter-spacing:.3px}
  .tab--about{left:0;top:364px;width:135px;padding-left:28px;border-radius:0 14px 14px 0}
  .tab--services{left:265px;top:387px;width:198px;padding-left:16px;border-radius:14px 0 0 14px}
  .tab--why{left:0;top:466px;width:185px;padding-left:24px;border-radius:0 14px 14px 0}
  .tab--reviews{left:243px;top:300px;width:220px;padding-left:18px;border-radius:14px 0 0 14px}

  .about{position:absolute;left:26px;top:399px;width:220px;font-size:8.6px;line-height:1.32}
  .services{position:absolute;left:270px;top:420px;list-style:none;font-size:8.8px;font-weight:700}
  .services li{height:15px;display:flex;align-items:center;gap:5px}
  .services li::before{content:"";width:8px;height:8px;border-radius:50%;background:var(--sky-soft);flex:none}
  .services .services__more{color:var(--sky-soft);padding-left:13px}
  .services .services__more::before{display:none}
  .reasons{position:absolute;left:26px;top:500px;list-style:none;font-size:8.2px;font-style:italic;font-weight:500}
  .reasons li{height:12.2px;display:flex;align-items:center;gap:4px}
  .tick{width:8px;height:8px;flex:none}

  .footer{position:absolute;left:0;bottom:0;width:463px;height:20px;background:var(--sky);display:flex;align-items:center;gap:6px;padding-left:12px;font-size:8.3px}
  .footer__dot{width:8px;height:8px;border-radius:50%;background:var(--white);flex:none}

  .copy{position:absolute;left:32px;top:304px;width:190px;font-size:8.2px;line-height:1.3}
  .copy p+p{margin-top:10px}
  .reviews{position:absolute;left:243px;top:336px;width:205px;font-size:8px;line-height:1.3}
  .review+.review{margin-top:8px}
  .review__name{display:block;text-align:right;color:var(--sky-soft);font-weight:700;margin-top:3px}

  .back-logo{position:absolute;left:14px;top:508px;width:100px;text-align:center;color:var(--white)}
  .back-logo .logo__mark{border-color:var(--white);width:28px;height:28px;border-width:2.5px}
  .back-logo .logo__name{font-size:12px;color:var(--white)}
  .request{position:absolute;left:118px;top:524px;color:var(--sky-soft);font-size:9px;font-weight:500}
  .back-call{position:absolute;left:118px;top:552px}
  .back-call__lead{font-size:11px;font-weight:500}
  .back-call__num{font-size:15.5px;font-weight:700;color:var(--sky-soft)}
  .back-links{position:absolute;left:300px;top:553px;list-style:none;font-size:7.2px;border-left:1px solid rgba(255,255,255,.5);padding-left:6px}
  .back-links li{height:12px;display:flex;align-items:center;gap:5px}
</style>
</head>
<body>
<div class="board">

  <!-- shared pieces defined once -->
  <svg width="0" height="0" style="position:absolute" aria-hidden="true">
    <defs>
      <linearGradient id="lowerFill" x1="0" y1="0" x2="0" y2="1">
        <stop offset="0" stop-color="#2c3f70"/>
        <stop offset="1" stop-color="#16224a"/>
      </linearGradient>
      <symbol id="front-shapes" viewBox="0 0 463 600">
        <path d="M0 0H463V56C420 60 370 78 300 104C190 146 100 80 0 122Z" fill="#fff"/>
        <path d="M0 126C100 84 190 150 300 110C370 84 420 66 463 62" fill="none" stroke="#1d2c57" stroke-width="12"/>
        <path d="M0 142C100 100 200 166 310 126C380 100 425 84 463 80" fill="none" stroke="#7f9fd9" stroke-width="5"/>
        <path d="M0 352C130 392 260 330 463 300V600H0Z" fill="url(#lowerFill)"/>
        <path d="M0 334C130 372 260 312 463 282" fill="none" stroke="#7f9fd9" stroke-width="7" opacity=".9"/>
      </symbol>
      <symbol id="back-shapes" viewBox="0 0 463 600">
        <path d="M0 196C120 240 260 190 463 150V600H0Z" fill="url(#lowerFill)"/>
        <path d="M0 182C120 226 260 176 463 136" fill="none" stroke="#7f9fd9" stroke-width="9"/>
        <path d="M0 210C120 254 260 204 463 164" fill="none" stroke="#1d2c57" stroke-width="6"/>
      </symbol>
      <symbol id="tick" viewBox="0 0 10 10">
        <circle cx="5" cy="5" r="4.2" fill="none" stroke="#fff" stroke-width="1"/>
        <path d="M3 5.2L4.5 6.6 7.2 3.6" fill="none" stroke="#fff" stroke-width="1.1"/>
      </symbol>
    </defs>
  </svg>

  <div class="label" style="left:22px">FRONT A</div>
  <div class="label" style="left:254px">FRONT B</div>
  <div class="label" style="left:487px">FRONT C</div>
  <div class="label" style="left:719px">FRONT D</div>
  <div class="label" style="left:952px">BACK</div>

  <!-- FRONT A -->
  <div class="sheet" style="left:22px">
    <article class="flyer">
      <div class="photo photo--speedboat" role="img" aria-label="Photo of a white motor yacht speeding across dark blue water"></div>
      <svg class="shapes" aria-hidden="true"><use href="#front-shapes"/></svg>
      <div class="logo"><span class="logo__mark"></span><span class="logo__name">KELPRIDGE HARBOR</span></div>
      <div class="contact-top"><div class="contact-top__lead">FOR MORE DETAILS</div><div class="contact-top__call">Call +1 845-555-0182</div></div>
      <h1 class="headline headline--stacked"><span class="headline__small">SPECIALIZED</span><span>MARINE</span><span>SERVICE</span></h1>
      <div class="circle circle--hull" role="img" aria-label="Photo of a boat hull wrapped in white shrink wrap"></div>
      <div class="circle circle--runabout" role="img" aria-label="Photo of a red and white runabout boat on a lake"></div>
      <div class="tab tab--about">ABOUT US</div>
      <p class="about">Kelpridge Harbor Services is a full mobile marine service capable of servicing all makes and models of inboard and outboard vessels. We offer dock side service, engine diagnostics, maintenance and repair, and much more</p>
      <div class="tab tab--services">OUR SERVICES</div>
      <ul class="services"><li>BOTTOM PAINTING</li><li>TEAK WORK</li><li>DETAILING</li><li>ELECTRICAL INSTALLS &amp; WIRING</li><li>MAINTENANCE &amp; REPAIRS</li><li>ENGINE DIAGNOSTICS</li><li>DOCK SIDE SERVICE</li><li>SHRINK WRAPPING</li><li>WINTERIZING &amp; SUMMERIZING</li><li class="services__more">AND MANY MORE....</li></ul>
      <div class="tab tab--why">WHY CHOOSE US</div>
      <ul class="reasons"><li><svg class="tick"><use href="#tick"/></svg>SPECIALIZES IN BOAT DIESEL ENGINES</li><li><svg class="tick"><use href="#tick"/></svg>HIGH QUALITY PRODUCTS</li><li><svg class="tick"><use href="#tick"/></svg>GUARANTEED WORK</li><li><svg class="tick"><use href="#tick"/></svg>EXCELLENT CUSTOMER SERVICES</li><li><svg class="tick"><use href="#tick"/></svg>LONG-STANDING REPUTATION</li><li><svg class="tick"><use href="#tick"/></svg>AFFORDABLE PRICING</li></ul>
      <div class="footer"><span class="footer__dot"></span>m.me/KelpridgeHarborServices<span class="footer__dot"></span>kelpridgeharbor@mailbox.com<span class="footer__dot"></span>need instagramlink</div>
    </article>
  </div>

  <!-- FRONT B -->
  <div class="sheet" style="left:254px">
    <article class="flyer">
      <div class="photo photo--yacht" role="img" aria-label="Photo of a large white luxury yacht cruising on grey sea"></div>
      <svg class="shapes" aria-hidden="true"><use href="#front-shapes"/></svg>
      <div class="logo"><span class="logo__mark"></span><span class="logo__name">KELPRIDGE HARBOR</span></div>
      <div class="contact-top"><div class="contact-top__lead">FOR MORE DETAILS</div><div class="contact-top__call">Call +1 845-555-0182</div></div>
      <h1 class="headline headline--wide"><span>SPECIALIZED</span><span>MARINE SERVICE</span></h1>
      <div class="circle circle--hull" role="img" aria-label="Photo of a boat hull wrapped in white shrink wrap"></div>
      <div class="circle circle--runabout" role="img" aria-label="Photo of a red and white runabout boat on a lake"></div>
      <div class="tab tab--about">ABOUT US</div>
      <p class="about">Kelpridge Harbor Services is a full mobile marine service capable of servicing all makes and models of inboard and outboard vessels. We offer dock side service, engine diagnostics, maintenance and repair, and much more</p>
      <div class="tab tab--services">OUR SERVICES</div>
      <ul class="services"><li>BOTTOM PAINTING</li><li>TEAK WORK</li><li>DETAILING</li><li>ELECTRICAL INSTALLS &amp; WIRING</li><li>MAINTENANCE &amp; REPAIRS</li><li>ENGINE DIAGNOSTICS</li><li>DOCK SIDE SERVICE</li><li>SHRINK WRAPPING</li><li>WINTERIZING &amp; SUMMERIZING</li><li class="services__more">AND MANY MORE....</li></ul>
      <div class="tab tab--why">WHY CHOOSE US</div>
      <ul class="reasons"><li><svg class="tick"><use href="#tick"/></svg>SPECIALIZES IN BOAT DIESEL ENGINES</li><li><svg class="tick"><use href="#tick"/></svg>HIGH QUALITY PRODUCTS</li><li><svg class="tick"><use href="#tick"/></svg>GUARANTEED WORK</li><li><svg class="tick"><use href="#tick"/></svg>EXCELLENT CUSTOMER SERVICES</li><li><svg class="tick"><use href="#tick"/></svg>LONG-STANDING REPUTATION</li><li><svg class="tick"><use href="#tick"/></svg>AFFORDABLE PRICING</li></ul>
      <div class="footer"><span class="footer__dot"></span>m.me/KelpridgeHarborServices<span class="footer__dot"></span>kelpridgeharbor@mailbox.com<span class="footer__dot"></span>need instagramlink</div>
    </article>
  </div>

  <!-- FRONT C -->
  <div class="sheet" style="left:487px">
    <article class="flyer">
      <div class="photo photo--harbor" role="img" aria-label="Photo of white yachts moored in a marina at golden sunset"></div>
      <svg class="shapes" aria-hidden="true"><use href="#front-shapes"/></svg>
      <div class="logo"><span class="logo__mark"></span><span class="logo__name">KELPRIDGE HARBOR</span></div>
      <div class="contact-top"><div class="contact-top__lead">FOR MORE DETAILS</div><div class="contact-top__call">Call +1 845-555-0182</div></div>
      <h1 class="headline headline--wide"><span>SPECIALIZED</span><span>MARINE SERVICE</span></h1>
      <div class="circle circle--hull" role="img" aria-label="Photo of a boat hull wrapped in white shrink wrap"></div>
      <div class="circle circle--runabout" role="img" aria-label="Photo of a red and white runabout boat on a lake"></div>
      <div class="tab tab--about">ABOUT US</div>
      <p class="about">Kelpridge Harbor Services is a full mobile marine service capable of servicing all makes and models of inboard and outboard vessels. We offer dock side service, engine diagnostics, maintenance and repair, and much more</p>
      <div class="tab tab--services">OUR SERVICES</div>
      <ul class="services"><li>BOTTOM PAINTING</li><li>TEAK WORK</li><li>DETAILING</li><li>ELECTRICAL INSTALLS &amp; WIRING</li><li>MAINTENANCE &amp; REPAIRS</li><li>ENGINE DIAGNOSTICS</li><li>DOCK SIDE SERVICE</li><li>SHRINK WRAPPING</li><li>WINTERIZING &amp; SUMMERIZING</li><li class="services__more">AND MANY MORE....</li></ul>
      <div class="tab tab--why">WHY CHOOSE US</div>
      <ul class="reasons"><li><svg class="tick"><use href="#tick"/></svg>SPECIALIZES IN BOAT DIESEL ENGINES</li><li><svg class="tick"><use href="#tick"/></svg>HIGH QUALITY PRODUCTS</li><li><svg class="tick"><use href="#tick"/></svg>GUARANTEED WORK</li><li><svg class="tick"><use href="#tick"/></svg>EXCELLENT CUSTOMER SERVICES</li><li><svg class="tick"><use href="#tick"/></svg>LONG-STANDING REPUTATION</li><li><svg class="tick"><use href="#tick"/></svg>AFFORDABLE PRICING</li></ul>
      <div class="footer"><span class="footer__dot"></span>m.me/KelpridgeHarborServices<span class="footer__dot"></span>kelpridgeharbor@mailbox.com<span class="footer__dot"></span>need instagramlink</div>
    </article>
  </div>

  <!-- FRONT D -->
  <div class="sheet" style="left:719px">
    <article class="flyer">
      <div class="photo photo--sail" role="img" aria-label="Photo of a sailboat deck and sail against a sunset over the sea"></div>
      <svg class="shapes" aria-hidden="true"><use href="#front-shapes"/></svg>
      <div class="logo"><span class="logo__mark"></span><span class="logo__name">KELPRIDGE HARBOR</span></div>
      <div class="contact-top"><div class="contact-top__lead">FOR MORE DETAILS</div><div class="contact-top__call">Call +1 845-555-0182</div></div>
      <h1 class="headline headline--wide headline--sail"><span>SPECIALIZED</span><span>MARINE SERVICE</span></h1>
      <div class="circle circle--hull" role="img" aria-label="Photo of a boat hull wrapped in white shrink wrap"></div>
      <div class="circle circle--runabout" role="img" aria-label="Photo of a red and white runabout boat on a lake"></div>
      <div class="tab tab--about">ABOUT US</div>
      <p class="about">Kelpridge Harbor Services is a full mobile marine service capable of servicing all makes and models of inboard and outboard vessels. We offer dock side service, engine diagnostics, maintenance and repair, and much more</p>
      <div class="tab tab--services">OUR SERVICES</div>
      <ul class="services"><li>BOTTOM PAINTING</li><li>TEAK WORK</li><li>DETAILING</li><li>ELECTRICAL INSTALLS &amp; WIRING</li><li>MAINTENANCE &amp; REPAIRS</li><li>ENGINE DIAGNOSTICS</li><li>DOCK SIDE SERVICE</li><li>SHRINK WRAPPING</li><li>WINTERIZING &amp; SUMMERIZING</li><li class="services__more">AND MANY MORE....</li></ul>
      <div class="tab tab--why">WHY CHOOSE US</div>
      <ul class="reasons"><li><svg class="tick"><use href="#tick"/></svg>SPECIALIZES IN BOAT DIESEL ENGINES</li><li><svg class="tick"><use href="#tick"/></svg>HIGH QUALITY PRODUCTS</li><li><svg class="tick"><use href="#tick"/></svg>GUARANTEED WORK</li><li><svg class="tick"><use href="#tick"/></svg>EXCELLENT CUSTOMER SERVICES</li><li><svg class="tick"><use href="#tick"/></svg>LONG-STANDING REPUTATION</li><li><svg class="tick"><use href="#tick"/></svg>AFFORDABLE PRICING</li></ul>
      <div class="footer"><span class="footer__dot"></span>m.me/KelpridgeHarborServices<span class="footer__dot"></span>kelpridgeharbor@mailbox.com<span class="footer__dot"></span>need instagramlink</div>
    </article>
  </div>

  <!-- BACK -->
  <div class="sheet" style="left:952px">
    <article class="flyer" style="background:var(--deep)">
      <div class="photo photo--engine" role="img" aria-label="Photo of a mechanic working on a boat diesel engine with a ratchet"></div>
      <svg class="shapes" aria-hidden="true"><use href="#back-shapes"/></svg>
      <h1 class="headline headline--engine"><span>SPECIALIZED</span><span>BOAT DIESEL</span><span>ENGINES</span></h1>
      <div class="circle circle--alternator" role="img" aria-label="Photo of an engine alternator and belt pulley"></div>
      <div class="circle circle--polisher" role="img" aria-label="Photo of a polishing tool buffing a boat surface"></div>
      <div class="copy">
        <p>We regularly service marine diesel engines of various vessel types. The overall footprint of the engine, as well as potential modifications to the stringers, exhaust, seawater and fuel piping must be carefully considered.</p>
        <p>When looking for a new engine model, review available installation requirements and engine specifications regarding exhaust back pressure limits, radiated heat, air consumption, seawater inlet restriction and fuel inlet restriction. These items are critical and may necessitate additional modifications to ensure proper installation.</p>
      </div>
      <div class="tab tab--reviews">CLIENT REVIEWS</div>
      <div class="reviews">
        <p class="review">They went above and beyond to make sure boat was well prepared for the season, greatly appreciated.<span class="review__name">Dale Whitcombe</span></p>
        <p class="review">Kelpridge Harbor Service, provides an excellent job, clean, organized and guaranteed. my boat had two years of not working, and I put it in the hands of Kelpridge Harbor Service Marine and they did an excellent job.<span class="review__name">Marco Ellery</span></p>
        <p class="review">Asked Ned to do a dirty job in a hurry as I needed boat in 2 days , he did it , fair price, neat , clean , job well done , I recommend him to everyone<span class="review__name">Tom Rudd</span></p>
      </div>
      <div class="back-logo"><span class="logo__mark"></span><span class="logo__name">KELPRIDGE HARBOR</span></div>
      <p class="request">PLEASE CONTACT US WITH ANY REQUESTS.</p>
      <div class="back-call"><div class="back-call__lead">FOR MORE DETAILS</div><div class="back-call__num">Call +1 845-555-0182</div></div>
      <ul class="back-links"><li><span class="footer__dot"></span>m.me/KelpridgeHarborServices</li><li><span class="footer__dot"></span>kelpridgeharbor@mailbox.com</li><li><span class="footer__dot"></span>need instagram link</li></ul>
    </article>
  </div>

</div>
</body>
</html>
```